Bourbon label design for bourbon brand. Looking to freshen our current label.

I need a Bourbon label design for our rebranded Bourbon bottle. Label should include picture of our horse and our logo on the bottle. Front Label is 3.5 inches wide and 6 inches tall, back label is 4 inches tall and 3 inches wide. Back label can be a simple plain logo like the one in the brief. I have included a design of our current bottle and label. We want to stay close to the current color schemes but want a fresh rebrand of the design. The label needs to be the correct size on a tall bottle like pictured.

Target Market(s)

Our Bourbon members, 30-50 year old males

Requirements
Must have
• Picture of our horse, our Ironhoof , straight Bourbon whiskey on the front. Room to edit text on the back label.

```html
<!DOCTYPE html>
<html lang="en">
<head>
<meta charset="utf-8">
<title>Ironhoof Straight Bourbon Whiskey – Front Label</title>
<link href="https://fonts.googleapis.com/css2?family=Bebas+Neue&family=Oswald:wght@500&display=swap" rel="stylesheet">
<style>
  :root {
    --page: #ffffff;
    --label: #151515;
    --label-edge: #0c0c0c;
    --gold: #b39a4c;
    --white: #f4f4f2;
    --photo-light: #8a8a8a;
    --photo-dark: #1e1e1e;
  }
  html, body {
    margin: 0;
    width: 1067px;
    height: 1200px;
    overflow: hidden;
    background: var(--page);
  }
  .canvas {
    position: relative;
    width: 1067px;
    height: 1200px;
  }
  .label {
    position: absolute;
    left: 308px;
    top: 50px;
    width: 450px;
    height: 1100px;
    overflow: hidden;
    background: linear-gradient(90deg, var(--label-edge) 0%, var(--label) 12%, #1d1d1d 50%, var(--label) 88%, var(--label-edge) 100%);
    font-family: "Oswald", sans-serif;
    color: var(--gold);
  }
  .horse-photo {
    position: absolute;
    left: 135px;
    top: 30px;
    width: 175px;
    height: 290px;
    border-radius: 45% 45% 30% 30%;
    background: radial-gradient(ellipse at 45% 35%, var(--photo-light) 0%, #4a4a4a 45%, var(--photo-dark) 100%);
  }
  .est {
    position: absolute;
    top: 232px;
    font-family: "Bebas Neue", sans-serif;
    font-size: 30px;
    color: var(--white);
    letter-spacing: 1px;
    border-bottom: 2px solid var(--gold);
    line-height: 1;
    padding-bottom: 3px;
  }
  .est-word { left: 66px; }
  .est-year { left: 345px; }
  .brand-title {
    position: absolute;
    left: 50%;
    top: 255px;
    font-family: "Bebas Neue", sans-serif;
    font-size: 330px;
    line-height: 1;
    color: var(--white);
    white-space: nowrap;
    transform: translateX(-50%) scaleX(0.42);
    transform-origin: center top;
  }
  .spirit-type {
    position: absolute;
    left: 0;
    top: 602px;
    width: 450px;
    text-align: center;
    font-family: "Bebas Neue", sans-serif;
    font-size: 44px;
    letter-spacing: 1px;
    line-height: 1;
    white-space: nowrap;
  }
  .brand-mark {
    position: absolute;
    left: 0;
    top: 740px;
    width: 450px;
    text-align: center;
    font-family: "Bebas Neue", sans-serif;
    font-size: 70px;
    line-height: 1;
    color: var(--white);
    letter-spacing: 1px;
  }
  .side-note {
    position: absolute;
    top: 752px;
    font-family: "Bebas Neue", sans-serif;
    font-size: 29px;
    line-height: 0.95;
    text-align: center;
  }
  .side-left { left: 18px; }
  .side-right { right: 14px; }
  .info-box {
    position: absolute;
    background: var(--white);
  }
  .info-box .tag {
    display: block;
    background: var(--gold);
    color: var(--label);
    font-family: "Bebas Neue", sans-serif;
    font-size: 16px;
    line-height: 19px;
    text-align: center;
  }
  .box-barrel { left: 20px; top: 925px; width: 62px; height: 72px; }
  .box-aged { left: 176px; top: 934px; width: 95px; height: 64px; }
  .box-abv { left: 367px; top: 925px; width: 61px; height: 72px; }
  .years {
    position: absolute;
    left: 176px;
    top: 1006px;
    width: 95px;
    text-align: center;
    font-family: "Bebas Neue", sans-serif;
    font-size: 20px;
  }
  .horseshoe {
    position: absolute;
    top: 947px;
    width: 38px;
    height: 40px;
  }
  .shoe-left { left: 107px; }
  .shoe-right { left: 300px; }
</style>
</head>
<body>
<div class="canvas">
  <div class="label">
    <div class="horse-photo" role="img" aria-label="Black and white photograph of the brand's racehorse and jockey galloping toward the viewer"></div>

    <span class="est est-word">EST</span>
    <span class="est est-year">2016</span>

    <div class="brand-title">IRONHOOF</div>
    <div class="spirit-type">STRAIGHT BOURBON WHISKEY</div>

    <div class="side-note side-left">SINGLE<br>BARREL</div>
    <div class="brand-mark">IRONHOOF</div>
    <div class="side-note side-right">BARREL<br>STRENGHT</div>

    <div class="info-box box-barrel"><span class="tag">BARREL NO.</span></div>
    <svg class="horseshoe shoe-left" viewBox="0 0 38 40" aria-hidden="true">
      <path d="M8 6 V20 A11 11 0 0 0 30 20 V6" fill="none" stroke="var(--gold)" stroke-width="5" stroke-linecap="round"/>
    </svg>
    <div class="info-box box-aged"><span class="tag">AGED</span></div>
    <div class="years">YEARS</div>
    <svg class="horseshoe shoe-right" viewBox="0 0 38 40" aria-hidden="true">
      <path d="M8 6 V20 A11 11 0 0 0 30 20 V6" fill="none" stroke="var(--gold)" stroke-width="5" stroke-linecap="round"/>
    </svg>
    <div class="info-box box-abv"><span class="tag">ALC/VOL</span></div>
  </div>
</div>
</body>
</html>
```